Business Card and Letterhead Design for Public Accounting Firm

Business card and letterhead design for a CPA Firm located in Orange County, CA. We're looking for a modern and professional design utilizing our existing logo. We'd like a clean "less is more" look, but also something that catches the eye. We provide a high level of service to our clients. Open to single or double sided business cards.

Additional info: color numbers on logo
Blue :
R 0
G 83
B 125

#00537D

Silver :

R 154
G 154
B 154

#9A9A9A

Target Market(s)

Businesses and individuals

Industry/Entity Type

Accounting

Contact Information for Business Card

Moss Whitfield & Danby LLP - 4827 Larkspur Vale Road, Irvine, CA 92614 - (949)731-2864 - mwdaccts.example

Font styles to use
Serif
Sans Serif
Other font styles liked:
• See font file uploaded

Colors
0054AA
0677BA
7BADD7
CADEEF
E8F1F8

Requirements
Nice to have
• Possibly use the font file provided which matches our logo, but adjust to be not in all caps

```html
<!DOCTYPE html>
<html lang="en">
<head>
<meta charset="utf-8">
<title>Moss Whitfield &amp; Danby LLP – Business Card</title>
<link rel="stylesheet" href="https://fonts.googleapis.com/css2?family=Cinzel:wght@500;600&family=Arimo:wght@400&display=swap">
<style>
  :root {
    --brand-blue: #0d5680;
    --brand-silver: #9a9a9a;
    --card-black: #000000;
    --card-white: #ffffff;
    --backdrop: #d9d9db;
    --serif: "Cinzel", "Times New Roman", serif;
    --sans: "Arimo", Arial, sans-serif;
  }
  html, body {
    margin: 0;
    width: 1200px;
    height: 1200px;
    overflow: hidden;
    background: var(--backdrop);
  }
  .canvas { position: relative; width: 1200px; height: 1200px; }

  .card {
    position: absolute;
    width: 906px;
    height: 520px;
    border-radius: 24px;
    overflow: hidden;
  }

  /* Front side */
  .card-front { left: 204px; top: 54px; background: var(--card-black); }
  .front-name {
    position: absolute;
    left: 0; right: 0; top: 200px;
    text-align: center;
    font-family: var(--serif);
    font-weight: 500;
    font-size: 40px;
    line-height: 1.15;
    letter-spacing: 3px;
    color: var(--card-white);
    margin: 0;
  }
  .front-web {
    position: absolute;
    left: 0; right: 0; top: 450px;
    text-align: center;
    font-family: var(--sans);
    font-size: 20px;
    letter-spacing: 8px;
    color: var(--card-white);
  }

  /* Back side */
  .card-back { left: 108px; top: 596px; background: var(--card-white); }
  .back-firm {
    position: absolute;
    left: 46px; top: 218px;
    font-family: var(--serif);
    font-weight: 500;
    font-size: 25px;
    line-height: 1.2;
    letter-spacing: 2px;
    color: var(--brand-blue);
    margin: 0;
  }
  .contact { position: absolute; left: 537px; top: 100px; color: var(--brand-blue); }
  .contact-name {
    margin: 0;
    font-family: var(--serif);
    font-weight: 600;
    font-size: 27px;
    letter-spacing: 0.5px;
  }
  .contact-title {
    margin: 6px 0 0;
    font-family: var(--serif);
    font-weight: 600;
    font-size: 19px;
  }
  .contact-address {
    margin: 46px 0 0;
    font-family: var(--sans);
    font-style: normal;
    font-size: 22px;
    line-height: 38px;
  }
  .contact-line {
    display: flex;
    align-items: center;
    gap: 6px;
    font-family: var(--sans);
    font-size: 22px;
    margin: 0;
  }
  .contact-phone { margin-top: 20px; }
  .contact-email { margin-top: 20px; }
  .icon { width: 18px; height: 16px; fill: var(--brand-blue); }

  .band-blue {
    position: absolute; left: 0; right: 0; bottom: 0;
    height: 27px; background: var(--brand-blue);
  }
  .band-silver {
    position: absolute; left: 426px; right: 10px; bottom: 11px;
    height: 16px; background: var(--brand-silver);
    border-left: 4px solid var(--card-white);
    border-bottom: 4px solid var(--card-white);
  }
</style>
</head>
<body>
<div class="canvas">
  <section class="card card-front">
    <h1 class="front-name">Moss Whitfield<br>&amp; Danby LLP</h1>
    <div class="front-web">www.mwdaccts.example</div>
  </section>

  <section class="card card-back">
    <p class="back-firm">Moss Whitfield<br>&amp; Danby LLP</p>
    <div class="contact">
      <h2 class="contact-name">Laura K. Benning</h2>
      <p class="contact-title">Manager</p>
      <address class="contact-address">4827 Larkspur Vale Road,<br>Irvine, CA 92614</address>
      <p class="contact-line contact-phone">
        <svg class="icon" viewBox="0 0 18 16" aria-hidden="true"><path d="M1 5c0-2 3-3 8-3s8 1 8 3v1h-4V4.5H5V6H1z"/><path d="M4 7h10l2 8H2z"/><circle cx="9" cy="11" r="2" fill="#fff"/></svg>
        (949)731-2864
      </p>
      <p class="contact-line contact-email">
        <svg class="icon" viewBox="0 0 18 16" aria-hidden="true"><rect x="1" y="3" width="16" height="11"/><path d="M1 3l8 6 8-6" fill="none" stroke="#fff" stroke-width="1.4"/></svg>
        office@mwdaccts.example
      </p>
    </div>
    <div class="band-blue"></div>
    <div class="band-silver"></div>
  </section>
</div>
</body>
</html>
```